Advertising tiles for website

Hi
I have a website at www.tagwhistle.co.nz and there are four spots along the top for advertising tiles (at the moment there are dummy tiles in place).

Each tile is 220 wide and 200 high and I would like 4 tiles created as a starting point for this site.

I can change the tiles on every page so conceivably we could have very targeted advertising leading the visitor to services we want to promote (we can set this extension up as a new design job for you). Eg. domains for sale, Escrow services, featured domains, Turnkey Websites, New Websites etc.

The advertisements that I might like see on the website would be as follows:
Gallery Ink
Sell Your Domain
Domains For Sale
Featured Domains
Buy Websites
Sell Your Website
Turnkey Websites
Trusted Escrow
New domains
News
Resources
note: the deliverable for this job is 4 tiles (not all of the above)as I want to get the design style sorted with you.

The website where these will appear sells pre-loved domains and turnkey websites. Also, some of these tiles will link through to a classifieds website which we will also want you to help create tiles for once this job is completed to satisfaction.

The files attached are samples only.

Target Market(s)

Domain buyers
Business owners
People buying websites

Industry/Entity Type

Advertising

Requirements
Must have
• Nice clean, clear text
Relevant
Nice to have
• Fun

```html
<!DOCTYPE html>
<html lang="en">
<head>
<meta charset="utf-8">
<title>Tagwhistle – Premium Domain Brokers</title>
<link href="https://fonts.googleapis.com/css2?family=Oswald:wght@400;500&family=Open+Sans:ital,wght@1,300;1,600&family=Arimo:ital,wght@0,400;0,700;1,700&display=swap" rel="stylesheet">
<style>
:root{
  --red:#8e0a0e;
  --red-dark:#6a0508;
  --red-bright:#c01a1f;
  --maroon:#7a0c10;
  --ink:#333;
  --grey:#555;
  --light:#f1f1f1;
  --line:#bbb;
  --white:#fff;
}
*{margin:0;padding:0;box-sizing:border-box}
html,body{width:1200px;height:900px;overflow:hidden;background:var(--white)}
.canvas{position:relative;width:1200px;height:900px;overflow:hidden;font-family:Arimo,Arial,sans-serif;
  background:linear-gradient(var(--white) 0 285px,#e6e6e6 286px,var(--white) 400px)}
.utility-bar{position:absolute;left:0;top:62px;width:1200px;height:37px;
  background:linear-gradient(var(--red-bright),var(--red-dark));}
.utility-links{position:absolute;right:44px;top:0;height:37px;display:flex;list-style:none}
.utility-links li{color:#f3d6d6;font-size:11.5px;padding:0 13px;line-height:37px;border-left:1px solid rgba(255,255,255,.35);transform:skewX(0)}
.page{position:absolute;left:60px;top:100px;width:1098px;height:800px;background:var(--white);border-left:1px solid #ddd;border-right:1px solid #ddd}
.masthead{position:absolute;left:68px;top:107px;width:1082px;height:136px;background:linear-gradient(#fafafa,#e9e9e9);overflow:hidden}
.masthead-art{position:absolute;left:0;top:0;width:372px;height:136px;background:linear-gradient(135deg,#e8e8e8,#c9c9c9 45%,#b01419 46%,#d9d9d9 90%)}
.masthead svg{position:absolute;left:0;top:0}
.brand{position:absolute;right:8px;top:90px;color:var(--white);font-family:Oswald,sans-serif;font-weight:500;font-size:33px;letter-spacing:2px;line-height:1}
.main-nav{position:absolute;left:0;top:249px;width:1200px;height:36px;background:linear-gradient(var(--red-bright),var(--red-dark))}
.main-nav ul{list-style:none;display:flex;position:absolute;left:87px;top:0}
.main-nav li{color:var(--white);font-weight:700;font-size:15px;line-height:37px;margin-right:45px}
.tile{position:absolute;top:296px;width:243px;height:85px;border-radius:5px;display:flex;align-items:center;
  font-family:Oswald,sans-serif;font-size:27px;box-shadow:0 1px 3px rgba(0,0,0,.35)}
.tile svg{margin:0 14px 0 22px;flex:none}
.tile-dark{background:linear-gradient(#a8494c,var(--red) 45%,var(--red-dark));color:var(--white);border:2px solid #d8b5b5}
.tile-light{background:linear-gradient(#fff,#e4e4e4);color:var(--maroon);border:2px solid #e7b0b2}
.tile-buy{left:80px}.tile-escrow{left:352px}.tile-resources{left:625px}.tile-news{left:897px}
.hero{position:absolute;left:67px;top:396px;width:1081px;height:187px;background:linear-gradient(90deg,#ede6dc,#e2d6c6 70%,#d6c7b4);overflow:hidden}
.hero-photo{position:absolute;right:0;top:0;width:290px;height:187px;background:linear-gradient(120deg,#e9e4dc,#c9b8a2 55%,#8b7b6a)}
.hero-title{position:absolute;left:16px;top:128px;font-family:"Open Sans",sans-serif;font-style:italic;font-weight:300;font-size:39px;letter-spacing:-1.5px;color:var(--maroon)}
.hero-title b{font-weight:600;color:#4a4a4a}
.content{position:absolute;left:78px;top:622px;width:1062px;color:var(--ink)}
.content h1{font-size:22px;color:var(--maroon);font-weight:700;line-height:30px}
.content h2{font-size:18px;color:var(--red-bright);font-weight:700;margin-top:8px;line-height:24px}
.quote{font-size:13px;color:var(--grey);margin-top:12px}
.quote em{font-weight:700;color:#444}
.links{list-style:disc;margin:12px 0 0 44px;font-size:13px;line-height:14.6px;color:var(--grey)}
.links a{color:var(--red-bright)}
.divider{border:0;border-top:1px dashed var(--line);margin:11px 0 9px}
.content h3{font-size:23px;color:var(--maroon);font-weight:700;line-height:28px}
.content h3 a{color:var(--red-bright)}
.points{list-style:disc;margin:10px 0 0 44px;font-size:13px;line-height:15px;color:var(--grey)}
</style>
</head>
<body>
<div class="canvas">
  <div class="utility-bar">
    <ul class="utility-links"><li>Home</li><li>Bookmark Site</li><li>Print</li><li>Tell a Friend</li><li>Contact Us</li></ul>
  </div>
  <div class="page"></div>
  <div class="masthead">
    <div class="masthead-art" role="img" aria-label="Illustration of small figures climbing large red WWW letters"></div>
    <svg width="1082" height="136"><polygon points="752,136 1082,0 1082,136" fill="#a90f14"/></svg>
    <div class="brand">TAGWHISTLE</div>
  </div>
  <nav class="main-nav"><ul><li>Home</li><li>Recent Sales</li><li>Search Listings</li><li>Register New Domain</li><li>Escrow</li><li>FAQ</li><li>Contact Us</li></ul></nav>

  <div class="tile tile-dark tile-buy">
    <svg width="56" height="44" viewBox="0 0 56 44" fill="none" stroke="#eee" stroke-width="3"><path d="M2 6h9l6 24h30l6-18H14"/><path d="M20 18h30M22 24h26"/><circle cx="21" cy="38" r="3.5" fill="#eee"/><circle cx="44" cy="38" r="3.5" fill="#eee"/></svg>
    Buy Websites</div>
  <div class="tile tile-light tile-escrow">
    <svg width="36" height="50" viewBox="0 0 36 50"><text x="18" y="42" text-anchor="middle" font-family="Arial,sans-serif" font-weight="700" font-size="48" fill="#a31418">$</text></svg>
    Trusted Escrow</div>
  <div class="tile tile-dark tile-resources">
    <svg width="50" height="46" viewBox="0 0 50 46"><path d="M3 10h16l4 5h24v28H3z" fill="#9aa6b5"/><rect x="3" y="18" width="44" height="25" fill="#c7d0da"/></svg>
    Resources</div>
  <div class="tile tile-light tile-news">
    <svg width="50" height="50" viewBox="0 0 50 50"><defs><radialGradient id="globe" cx=".35" cy=".3"><stop offset="0" stop-color="#bfe0ff"/><stop offset="1" stop-color="#1c5fb0"/></radialGradient></defs><circle cx="25" cy="25" r="23" fill="url(#globe)"/></svg>
    <span style="margin-left:36px">News</span></div>

  <section class="hero">
    <div class="hero-photo" role="img" aria-label="Photograph of two colleagues smiling at a laptop"></div>
    <p class="hero-title">Premium <b>Domain</b> Brokers</p>
  </section>

  <main class="content">
    <h1>Tagwhistle.co.nz Ranked #1 on Searchly NZ Search</h1>
    <h2>Selling Premium Domains &amp; Websites Since 2003</h2>
    <p class="quote"><em>"Domains have and will continue to go up in value faster than any other commodity EVER known to man."</em> Harold Brink, Brinkware Corp</p>
    <ul class="links">
      <li><a>Browse listings in alphabetical order</a></li>
      <li><a>Browse listings in price order</a></li>
      <li>Looking for something suitable to your industry or interests? <a>Browse listings in category order</a></li>
      <li>Like to know how much domains have been selling for?&nbsp; Check out <a>2010 top international sales</a> and <a>some of NZ's sales</a></li>
    </ul>
    <hr class="divider">
    <h3>Domain names are virtual real estate and hugely valuable.&nbsp; Check out some <a>recent sales </a>and the <a>top 100 sales</a></h3>
    <ul class="points">
      <li>Your domain name greatly influences search engine results.</li>
      <li>Your premium domain gives your business a head start online.</li>
    </ul>
  </main>
</div>
</body>
</html>
```